Business Card Design Project

We need a redesign of our business card.
We are a Consulting Property Developer called The Kestrel Group
Updates

Thank you all for submissions. Just waiting on managment to decide.

Thank you,

Dorinda

Industry/Entity Type

Business

Requirements
Must have
• we like having the KG a focus in the back ground or on the side
Kestrel is our company colour

the wording - property development
and - premium accommodation

our website www.kestrelgroup-example.com.au

persons name
title

p: 1300 482917 f: 1300 482915 m: 0417593824
PO Box 5817, Brindlevale Qld 4178
e: admin@kestrelgroup-example.com.au

```html
<!DOCTYPE html>
<html lang="en">
<head>
<meta charset="utf-8">
<title>The Kestrel Group – Business Card</title>
<link href="https://fonts.googleapis.com/css2?family=Marcellus&display=swap" rel="stylesheet">
<style>
  :root {
    --card-deep: #4a0a0c;
    --card-mid: #8a1a1c;
    --card-light: #a8383a;
    --band-light: rgba(255, 240, 236, 0.55);
    --brand-ink: #6e0f18;
    --text-cream: #fff4e6;
    --text-glow: rgba(30, 0, 0, 0.9);
    --mark-faint: rgba(255, 225, 225, 0.28);
  }
  * { margin: 0; padding: 0; box-sizing: border-box; }
  html, body {
    width: 1200px;
    height: 748px;
    overflow: hidden;
    background: #ffffff;
  }
  .card {
    position: relative;
    width: 1200px;
    height: 748px;
    overflow: hidden;
    font-family: "Marcellus", "Optima", serif;
    color: var(--text-cream);
  }
  .card__scene {
    position: absolute;
    inset: 0;
    background:
      radial-gradient(ellipse at 55% 35%, var(--card-light) 0%, transparent 60%),
      linear-gradient(180deg, var(--card-mid) 0%, #7a1416 45%, var(--card-deep) 100%);
  }
  .brand-band {
    position: absolute;
    left: 0;
    top: 53px;
    width: 1200px;
    height: 145px;
    background: linear-gradient(90deg, var(--band-light) 0%, rgba(255,240,236,0.4) 60%, rgba(255,240,236,0.15) 100%);
  }
  .brand-name {
    position: absolute;
    left: 74px;
    top: 62px;
    font-size: 116px;
    line-height: 1;
    color: var(--brand-ink);
    white-space: nowrap;
  }
  .person {
    position: absolute;
    left: 137px;
    top: 236px;
    text-shadow: 0 0 8px var(--text-glow), 0 0 3px var(--text-glow);
  }
  .person__name {
    font-size: 46px;
    line-height: 1;
  }
  .person__title {
    margin-top: 14px;
    margin-left: 74px;
    font-size: 26px;
    line-height: 1;
  }
  .services {
    position: absolute;
    right: 40px;
    top: 232px;
    list-style: none;
    text-align: right;
    font-size: 30px;
    line-height: 44px;
    text-shadow: 0 0 8px var(--text-glow), 0 0 3px var(--text-glow);
  }
  .contact {
    position: absolute;
    left: 74px;
    top: 432px;
    list-style: none;
    font-size: 32px;
    line-height: 52px;
    text-shadow: 0 0 8px var(--text-glow), 0 0 3px var(--text-glow);
  }
  .contact__gap { margin-left: 14px; }
  .contact__email { margin-top: 8px; }
  .monogram {
    position: absolute;
    left: 780px;
    top: 515px;
    font-size: 118px;
    line-height: 1;
    color: var(--mark-faint);
  }
  .website {
    position: absolute;
    right: 34px;
    top: 676px;
    font-size: 37px;
    line-height: 1;
    white-space: nowrap;
    text-shadow: 0 0 8px var(--text-glow), 0 0 3px var(--text-glow);
  }
</style>
</head>
<body>
  <main class="card">
    <div class="card__scene" role="img" aria-label="Maroon-toned photograph of a construction site with crane and building silhouettes"></div>

    <div class="brand-band"></div>
    <div class="brand-name">The Kestrel Group</div>

    <section class="person">
      <div class="person__name">persons name</div>
      <div class="person__title">title</div>
    </section>

    <ul class="services">
      <li>property development</li>
      <li>premium accommodation</li>
    </ul>

    <ul class="contact">
      <li>p: 1300 482917 <span class="contact__gap">f: 1300 482915</span></li>
      <li>m: 0417593824</li>
      <li>PO Box 5817, Brindlevale Qld 4178</li>
      <li class="contact__email">e: admin@kestrelgroup-example.com.au</li>
    </ul>

    <div class="monogram">KG</div>

    <div class="website">www.kestrelgroup-example.com.au</div>
  </main>
</body>
</html>
```